Brimovex business card

Based on company logo and website given , to design a business card temple. Slogan "Your furry friends deserves the best"
Color style please refer to our website

```html
<!DOCTYPE html>
<html lang="en">
<head>
<meta charset="utf-8">
<title>Brimovex business card</title>
<link rel="stylesheet" href="https://fonts.googleapis.com/css2?family=Montserrat:wght@400;500;600&display=swap">
<style>
  :root {
    --page-bg: #bdbdbd;
    --card-bg: #000000;
    --gold: #c1af2e;
    --blue: #0e68bf;
    --white: #ffffff;
  }
  html, body {
    margin: 0;
    padding: 0;
    width: 1200px;
    height: 1200px;
    overflow: hidden;
    background: var(--page-bg);
    font-family: "Montserrat", sans-serif;
  }
  .card {
    position: absolute;
    left: 231px;
    width: 746px;
    height: 425px;
    background: var(--card-bg);
    overflow: hidden;
  }
  .card--front { top: 141px; }
  .card--back { top: 642px; }

  .wordmark {
    position: absolute;
    margin: 0;
    color: var(--gold);
    font-weight: 500;
    line-height: 1;
    letter-spacing: 0.5px;
  }
  .card--front .wordmark {
    left: 41px;
    top: 78px;
    font-size: 48px;
  }
  .card--back .wordmark {
    left: 0;
    right: 0;
    top: 214px;
    text-align: center;
    font-size: 80px;
  }

  .person {
    position: absolute;
    right: 40px;
    top: 180px;
    text-align: right;
  }
  .person__name {
    margin: 0;
    color: var(--gold);
    font-size: 25px;
    font-weight: 600;
    letter-spacing: 1.2px;
    line-height: 30px;
  }
  .person__title {
    margin: 0;
    color: var(--white);
    font-size: 18px;
    font-weight: 400;
    line-height: 24px;
    letter-spacing: 0.5px;
  }

  .divider {
    position: absolute;
    left: 41px;
    top: 250px;
    width: 665px;
    height: 1px;
    background: var(--gold);
  }

  .contacts {
    position: absolute;
    left: 41px;
    top: 283px;
    margin: 0;
    padding: 0;
    list-style: none;
  }
  .contacts li {
    display: flex;
    align-items: center;
    height: 25px;
    color: var(--white);
    font-size: 18px;
    letter-spacing: 0.4px;
  }
  .contacts svg {
    width: 13px;
    height: 13px;
    margin-right: 8px;
    flex: none;
  }

  .address {
    position: absolute;
    right: 40px;
    top: 300px;
    margin: 0;
    text-align: right;
    color: var(--white);
    font-size: 18px;
    font-style: normal;
    line-height: 25px;
    letter-spacing: 0.6px;
  }

  .bands {
    position: absolute;
    left: 0;
    top: 0;
    width: 746px;
    height: 425px;
  }

  .tagline {
    position: absolute;
    left: 0;
    right: 0;
    top: 377px;
    margin: 0;
    text-align: center;
    color: var(--white);
    font-size: 18px;
    letter-spacing: 0.6px;
  }
</style>
</head>
<body>

<section class="card card--front">
  <p class="wordmark">Brimovex</p>

  <div class="person">
    <p class="person__name">DANIEL HART</p>
    <p class="person__title">Director</p>
  </div>

  <div class="divider"></div>

  <ul class="contacts">
    <li>
      <svg viewBox="0 0 16 16" aria-hidden="true"><path d="M4 1.5 6.2 4.2 5 6c.9 2 2.3 3.6 4.2 4.8l1.6-1.2 2.7 2.1-1.3 2.5C7.5 14 2.4 8.5 2 3z" fill="var(--gold)"/></svg>
      702.555.0148
    </li>
    <li>
      <svg viewBox="0 0 16 16" aria-hidden="true"><rect x="4" y="1.5" width="8" height="4" fill="var(--gold)"/><rect x="1" y="6" width="14" height="6" rx="1" fill="var(--gold)"/><rect x="4" y="10" width="8" height="4.5" fill="var(--gold)" stroke="#000" stroke-width="1"/></svg>
      702-555-0149
    </li>
    <li>
      <svg viewBox="0 0 16 16" aria-hidden="true"><rect x="1.5" y="3.5" width="13" height="9" fill="none" stroke="var(--gold)" stroke-width="1.5"/><path d="M1.5 3.5 8 9l6.5-5.5" fill="none" stroke="var(--gold)" stroke-width="1.5"/></svg>
      info@Brimovex.com
    </li>
    <li>
      <svg viewBox="0 0 16 16" aria-hidden="true"><g fill="none" stroke="var(--gold)" stroke-width="1.1"><circle cx="8" cy="8" r="6.5"/><ellipse cx="8" cy="8" rx="3" ry="6.5"/><path d="M1.5 8h13M2.5 4.8h11M2.5 11.2h11"/></g></svg>
      www.Brimovex.com
    </li>
  </ul>

  <address class="address">
    418 W. Alder Ave #210<br>
    Larkfield, NV 89120
  </address>

  <svg class="bands" viewBox="0 0 746 425" aria-hidden="true">
    <polygon points="0,413 399,413 391,425 0,425" fill="var(--gold)"/>
    <polygon points="428,385 746,385 746,425 403,425" fill="var(--blue)"/>
  </svg>
</section>

<section class="card card--back">
  <p class="wordmark">Brimovex</p>
  <p class="tagline">YOUR FURRY FRIENDS DESERVES THE BEST</p>
</section>

</body>
</html>
```